Contemporary Elegant Business Card Design for an International Trade Company in the Wine Industry

We need a new business card design for an international trade company in the wine and winemaking industry. The overall feel of the card should be contemporary, upscale, luxurious and elegant. It should communicate confidence and professionalism. The colors should complementary to our logo design (burgundy, gold, and black).
Inspiration: rich velvet tapestry
The card should include the following information:
Business: Brovenna Trading/Shipping, LLC.
Name: Marcus T. Hollenbrand
Title: CEO
Email: mark@brovennatrading.example
Phone: 555-294-6172
www.brovennatrading.example
Updates
Project Deadline Extended
Reason: We'd like the designers that we requested some additional designs from to still submit designs. Thank you!
Industry/Entity Type
Business
Contact Information for Business Card
Title: CEO
Phone: 555-294-6172
www.brovennatrading.example
Look and feel

```html
<!DOCTYPE html>
<html lang="en">
<head>
<meta charset="utf-8">
<title>Brovenna Trading – Business Card</title>
<link rel="stylesheet" href="https://fonts.googleapis.com/css2?family=Sorts+Mill+Goudy:ital@0;1&display=swap">
<style>
  :root {
    --backdrop: #3a0b10;
    --card-burgundy: #7c1521;
    --card-burgundy-deep: #661019;
    --gold: #d79a2b;
    --gold-soft: #c98d2a;
    --ivory: #f1e6dc;
    --wine-red: #a3182a;
  }
  * { margin: 0; padding: 0; box-sizing: border-box; }
  html, body { width: 1200px; height: 1200px; overflow: hidden; }
  body {
    background: var(--backdrop);
    font-family: "Sorts Mill Goudy", Georgia, serif;
    position: relative;
  }
  .card {
    position: absolute;
    left: 220px;
    width: 760px;
    height: 434px;
    background: radial-gradient(ellipse at 40% 35%, var(--card-burgundy) 0%, var(--card-burgundy-deep) 100%);
    box-shadow: 0 18px 40px rgba(0,0,0,0.45);
    overflow: hidden;
  }
  .card--back { top: 150px; }
  .card--front { top: 620px; }

  /* Back side */
  .contact {
    position: absolute;
    left: 64px;
    top: 110px;
    font-style: italic;
  }
  .contact__name { color: var(--gold); font-size: 34px; line-height: 1.1; }
  .contact__title { color: var(--gold); font-style: normal; font-size: 20px; letter-spacing: 1px; margin-top: 2px; }
  .contact__details { margin-top: 36px; color: var(--ivory); font-size: 19px; line-height: 1.55; }
  .contact__web {
    position: absolute;
    left: 64px;
    bottom: 48px;
    color: var(--ivory);
    font-style: italic;
    font-size: 19px;
  }
  .pour-illustration {
    position: absolute;
    right: 90px;
    top: 0;
    width: 200px;
    height: 380px;
  }

  /* Front side */
  .brand {
    position: absolute;
    left: 50%;
    top: 50%;
    transform: translate(-50%, -50%);
    display: flex;
    flex-direction: column;
    align-items: center;
    gap: 18px;
  }
  .brand__mark {
    width: 150px;
    height: 150px;
    background: var(--gold-soft);
  }
  .brand__name {
    color: var(--ivory);
    font-size: 34px;
    letter-spacing: 2px;
    text-align: center;
    line-height: 1.1;
  }
</style>
</head>
<body>

  <section class="card card--back">
    <div class="contact">
      <p class="contact__name">Marcus T. Hollenbrand</p>
      <p class="contact__title">CEO</p>
      <div class="contact__details">
        <p>Brovenna Trading/Shipping, LLC.</p>
        <p>mark@brovennatrading.example</p>
        <p>Tel: 555-294-6172</p>
      </div>
    </div>
    <p class="contact__web">www.brovennatrading.example</p>

    <svg class="pour-illustration" viewBox="0 0 200 380" role="img" aria-label="Illustration of red wine pouring from a bottle into a wine glass">
      <defs>
        <linearGradient id="pourTone" x1="0" y1="0" x2="0" y2="1">
          <stop offset="0" stop-color="#d79a2b" stop-opacity="0.55"/>
          <stop offset="0.5" stop-color="#a3182a" stop-opacity="0.8"/>
          <stop offset="1" stop-color="#d79a2b" stop-opacity="0.5"/>
        </linearGradient>
      </defs>
      <rect x="0" y="0" width="200" height="380" rx="6" fill="url(#pourTone)"/>
    </svg>
  </section>

  <section class="card card--front">
    <div class="brand">
      <div class="brand__mark" aria-hidden="true"></div>
      <p class="brand__name">BROVENNA TRADING AND SHIPPING</p>
    </div>
  </section>

</body>
</html>
```